OAKandRIVER Learning & Development
Business card, Letterhead & Compliment Slip design
Simple
Mara Hollings
Director
41 Fennick Row
Ashbury
North Wessex KX4 7RB
mhollings@oakandriverltd-example.co.uk
www.oakandriverltd-example.co.uk
Letterhead needs to be UK standard size A4 and used electronically, therefore, not too heavy on printer toner.
Compliment slip needs to be DL size which is 110mm x 220mm.
We are open to your ideas on this, it could be that the logo is on the front and all other details on reverse side.
We would like to see your ideas please.
Please see attached file for our logo, to be included in this design project. Many thanks.

```html
<!DOCTYPE html>
<html lang="en">
<head>
<meta charset="utf-8">
<title>Oak and River Stationery</title>
<link href="https://fonts.googleapis.com/css2?family=Raleway:wght@300;400;500&display=swap" rel="stylesheet">
<style>
  :root {
    --board: #a6a8ab;
    --paper: #ffffff;
    --ink: #4a4a4a;
    --ink-soft: #7a7a7a;
    --gold-light: #e9cf86;
    --gold: #c49a3a;
    --gold-dark: #8d6a1f;
    --fold: #d4d4d4;
  }
  * { box-sizing: border-box; margin: 0; padding: 0; }
  html, body { width: 1200px; height: 655px; overflow: hidden; }
  body { background: var(--board); font-family: "Raleway", sans-serif; color: var(--ink); }
  .canvas { position: relative; width: 1200px; height: 655px; }
  .sheet { position: absolute; background: var(--paper); box-shadow: 0 1px 3px rgba(0,0,0,.18); overflow: hidden; }

  .wordmark { line-height: 1; }
  .wordmark__name { display: block; font-weight: 400; color: var(--ink); letter-spacing: .04em; white-space: nowrap; }
  .wordmark__tag { display: block; font-weight: 300; color: var(--ink-soft); letter-spacing: .08em; margin-top: 4px; white-space: nowrap; }

  .rings {
    position: absolute;
    background: radial-gradient(circle at 35% 30%, var(--gold-light), var(--gold) 55%, var(--gold-dark));
    border-radius: 50% 0 0 0;
  }

  .contact { position: absolute; font-size: 6px; line-height: 1.6; color: var(--ink-soft); font-weight: 400; white-space: nowrap; }
  .web { position: absolute; font-size: 5.5px; color: var(--ink); font-weight: 500; white-space: nowrap; }

  /* Letterhead */
  .letterhead { left: 187px; top: 17px; width: 401px; height: 612px; }
  .letterhead .web { right: 22px; top: 16px; }
  .letterhead .wordmark { position: absolute; left: 22px; top: 72px; }
  .letterhead .wordmark__name { font-size: 15px; }
  .letterhead .wordmark__tag { font-size: 5px; }
  .letterhead .contact { left: 22px; top: 512px; }
  .letterhead .rings { right: 0; bottom: 0; width: 120px; height: 170px; }

  /* Business cards */
  .card { left: 14px; width: 163px; height: 100px; }
  .card--front { top: 211px; }
  .card--back { top: 325px; }
  .card--front .wordmark { position: absolute; left: 12px; top: 40px; }
  .card--front .wordmark__name { font-size: 10px; }
  .card--front .wordmark__tag { font-size: 4px; }
  .card--front .rings { right: 0; bottom: 0; width: 52px; height: 100px; }
  .card--back .person { position: absolute; left: 8px; top: 12px; font-size: 5.5px; line-height: 1.5; }
  .card--back .person__name { font-weight: 500; color: var(--gold); }
  .card--back .person__role { color: var(--ink-soft); }
  .card--back .contact { left: 64px; top: 12px; font-size: 4.5px; }
  .card--back .contact--mail { left: 8px; top: 76px; }
  .card--back .rings { right: 0; bottom: 0; width: 40px; height: 100px; }

  /* Envelope reverse */
  .envelope { left: 677px; top: 67px; width: 499px; height: 250px; }
  .envelope__flap { position: absolute; inset: 0; }

  /* Compliment slip */
  .slip { left: 677px; top: 353px; width: 499px; height: 252px; }
  .slip .web { right: 20px; top: 16px; }
  .slip .wordmark { position: absolute; left: 20px; top: 80px; }
  .slip .wordmark__name { font-size: 14px; }
  .slip .wordmark__tag { font-size: 5px; }
  .slip .contact { left: 20px; top: 186px; }
  .slip .rings { right: 0; bottom: 0; width: 110px; height: 170px; }
</style>
</head>
<body>
<main class="canvas">

  <section class="sheet card card--front">
    <div class="wordmark">
      <span class="wordmark__name">Oak and River</span>
      <span class="wordmark__tag">LEARNING &amp; DEVELOPMENT</span>
    </div>
    <div class="rings" role="img" aria-label="Gold ring decoration"></div>
  </section>

  <section class="sheet card card--back">
    <div class="person">
      <div class="person__name">Mara Hollings</div>
      <div class="person__role">Director</div>
    </div>
    <div class="contact">
      T 01632 960 214<br>M 07700 900 318<br>41 Fennick Row<br>Ashbury<br>North Wessex KX4 7RB
    </div>
    <div class="contact contact--mail">mhollings@oakandriverltd-example.co.uk<br>www.oakandriverltd-example.co.uk</div>
    <div class="rings" role="img" aria-label="Gold ring decoration"></div>
  </section>

  <section class="sheet letterhead">
    <div class="web">www.oakandriverltd-example.co.uk</div>
    <div class="wordmark">
      <span class="wordmark__name">Oak and River</span>
      <span class="wordmark__tag">LEARNING &amp; DEVELOPMENT</span>
    </div>
    <div class="contact">
      T 01632 960 214<br>M 07700 900 318<br><br>mhollings@oakandriverltd-example.co.uk<br><br>41 Fennick Row Ashbury North Wessex KX4 7RB
    </div>
    <div class="rings" role="img" aria-label="Gold ring decoration"></div>
  </section>

  <section class="sheet envelope">
    <svg class="envelope__flap" viewBox="0 0 499 250" preserveAspectRatio="none" aria-hidden="true">
      <polyline points="0,4 14,4 230,118 269,118 485,4 499,4" fill="none" stroke="var(--fold)" stroke-width="1.5"/>
      <path d="M230,118 Q249.5,130 269,118" fill="none" stroke="var(--fold)" stroke-width="1.5"/>
    </svg>
  </section>

  <section class="sheet slip">
    <div class="web">www.oakandriverltd-example.co.uk</div>
    <div class="wordmark">
      <span class="wordmark__name">Oak and River</span>
      <span class="wordmark__tag">LEARNING &amp; DEVELOPMENT</span>
    </div>
    <div class="contact">
      T 01632 960 214<br>M 07700 900 318<br><br>mhollings@oakandriverltd-example.co.uk<br><br>41 Fennick Row Ashbury North Wessex KX4 7RB
    </div>
    <div class="rings" role="img" aria-label="Gold ring decoration"></div>
  </section>

</main>
</body>
</html>
```